Eye-Catching, Direct Marketing Residential Painting Flyer!

I am run a residential painting business and am looking for a flyer to be designed to mailout to potential customers.
I want the copy/wording to be designed similar to this flyer.

It's important that the person reading the flyer gets the benefits we're promoting which is why I want the wording/copy to be almost identical to the flyer attached.

However, the structure will be different. The flyer will be a postcard thick, 5 x11.5.
Double sided.

The name of the company is Brightwall Coaters.

I would also like the prominent colour to either be light green or orange.

Target Market(s)

Home Owners between the age of 45-80.

Industry/Entity Type

Painting And Decorating

Font styles to use
Serif

Colors
f68d4d
faa54b
f78f20
f37122
9bcb3c
abd037
cadf82

Requirements
Must have
• Excellent Eye-Catching Design
• Benefits Visibly Promoted
• Action Taking Incentive- Call Now for FREE Window Cleaning and FREE Painting Estimate
Should not have
• Crowded wording

```html
<!DOCTYPE html>
<html lang="en">
<head>
<meta charset="utf-8">
<title>Brightwall Coaters – Postcard</title>
<link rel="stylesheet" href="https://fonts.googleapis.com/css2?family=Roboto+Condensed:wght@400;700&family=Open+Sans:wght@400;700&display=swap">
<style>
  :root {
    --orange: #f37122;
    --orange-soft: #f78f20;
    --green: #9bcb3c;
    --green-light: #cadf82;
    --ink: #231f20;
    --paper: #ffffff;
    --backdrop: #e9e9e9;
    --rule: #8a8a8a;
  }
  * { margin: 0; padding: 0; box-sizing: border-box; }
  html, body { width: 1200px; height: 1115px; overflow: hidden; background: var(--backdrop); }
  .canvas { position: relative; width: 1200px; height: 1115px; }
  .card {
    position: absolute; left: 100px; width: 828px; height: 420px;
    transform: scale(1.2077); transform-origin: top left;
    background: var(--paper); overflow: hidden;
    font-family: "Open Sans", sans-serif; color: var(--ink);
    box-shadow: 0 2px 8px rgba(0,0,0,.18);
  }
  .card--front { top: 38px; }
  .card--back { top: 578px; }
  .card-shapes { position: absolute; inset: 0; }
  .condensed { font-family: "Roboto Condensed", sans-serif; font-weight: 700; }

  /* front */
  .headline { position: absolute; left: 438px; top: 36px; width: 280px; text-align: center; font-size: 19px; line-height: 1.2; }
  .headline .word-clean { color: var(--orange); }
  .headline .word-fresh { color: var(--green); }
  .brand { position: absolute; text-align: center; }
  .brand-ring { display: block; margin: 0 auto 6px; width: 96px; height: 96px; border-radius: 50%; border: 6px solid var(--green); background: var(--paper); }
  .brand-name { font-family: "Roboto Condensed", sans-serif; font-weight: 700; color: var(--orange); font-size: 18px; white-space: nowrap; }
  .card--front .brand { left: 690px; top: 10px; width: 130px; }
  .offer-tag { position: absolute; left: 494px; top: 148px; width: 212px; height: 48px; background: var(--orange); border-radius: 4px; color: var(--paper); font-size: 27px; text-align: center; line-height: 48px; }
  .offer-list { position: absolute; left: 464px; top: 222px; width: 262px; list-style: none; font-size: 8.6px; line-height: 1.45; text-align: justify; }
  .offer-list li { position: relative; padding-left: 12px; margin-bottom: 14px; }
  .offer-list li::before { content: ""; position: absolute; left: 0; top: 4px; width: 4px; height: 4px; border-radius: 50%; background: var(--orange); }
  .call-offer { position: absolute; left: 393px; top: 350px; font-size: 17px; line-height: 1.28; color: var(--ink); }
  .call-divider { position: absolute; left: 620px; top: 352px; width: 1.5px; height: 60px; background: var(--ink); }
  .phone-front { position: absolute; left: 638px; top: 364px; font-size: 27px; color: var(--ink); }

  /* back */
  .issue-panel { position: absolute; left: 0; top: 0; width: 378px; height: 345px; background: var(--orange); color: var(--paper); }
  .panel-tag { display: block; margin: 0 auto; width: 128px; height: 32px; border-radius: 4px; background: var(--green); color: var(--paper); font-size: 17px; text-align: center; line-height: 32px; }
  .panel-tag--problem { margin-top: 18px; }
  .panel-tag--solution { margin-top: 8px; }
  .issue-list { list-style: none; padding: 10px 22px 0 28px; font-size: 8.2px; line-height: 1.45; }
  .issue-list li { position: relative; padding-left: 8px; margin-bottom: 9px; }
  .issue-list li::before { content: ""; position: absolute; left: -4px; top: 4px; width: 3px; height: 3px; border-radius: 50%; background: var(--paper); }
  .call-band { position: absolute; left: 0; top: 345px; width: 378px; height: 75px; background: var(--green); text-align: center; color: var(--ink); }
  .call-band .call-label { display: block; margin-top: 10px; font-size: 19px; line-height: 1; }
  .call-band .phone-back { display: block; font-size: 30px; line-height: 1.1; }
  .card--back .brand { left: 410px; top: 22px; width: 120px; }
  .stamp-box { position: absolute; left: 707px; top: 22px; width: 88px; height: 86px; border: 1px solid var(--ink); }
  .address-line { position: absolute; left: 470px; width: 325px; height: 1px; background: var(--rule); }
</style>
</head>
<body>
<main class="canvas">

  <section class="card card--front">
    <svg class="card-shapes" viewBox="0 0 828 420" width="828" height="420" aria-hidden="true">
      <defs>
        <linearGradient id="photo-tone" x1="0" y1="0" x2="1" y2="1">
          <stop offset="0" stop-color="#f1efeb"/>
          <stop offset="0.55" stop-color="#d9d4cb"/>
          <stop offset="1" stop-color="#3a4358"/>
        </linearGradient>
      </defs>
      <rect x="360" y="342" width="468" height="78" fill="var(--green)"/>
      <path d="M368 0 H392 C470 110 458 255 398 326 L828 324 V334 L388 338 C446 250 448 110 368 0 Z" fill="var(--orange)"/>
      <path d="M314 0 H366 C446 110 440 285 346 420 H318 C412 290 410 110 314 0 Z" fill="var(--green)"/>
      <path d="M0 0 H306 C400 110 400 290 310 420 H0 Z" fill="url(#photo-tone)" role="img" aria-label="Photo of a painter rolling paint onto a white wall"/>
    </svg>

    <h1 class="headline condensed">We make your home look <span class="word-clean">CLEAN</span>,<br><span class="word-fresh">FRESH</span> &amp; Beautiful again!</h1>

    <div class="brand">
      <span class="brand-ring"></span>
      <span class="brand-name">Brightwall Coaters</span>
    </div>

    <div class="offer-tag condensed">Special Offer!</div>

    <ul class="offer-list">
      <li>If you are one of the <b>first 17 exterior projects</b> that book with us, you will receive a complimentary window cleaning!</li>
      <li>If you are one of the <b>first 13 exterior projects</b> that book with us, you will receive a complimentary interior design consultation by a professional interior designer!</li>
    </ul>

    <p class="call-offer condensed">Call Now for<br>FREE Window Cleaning and<br>FREE Painting Estimate</p>
    <span class="call-divider"></span>
    <p class="phone-front condensed">555-013-4821</p>
  </section>

  <section class="card card--back">
    <div class="issue-panel">
      <h2 class="panel-tag panel-tag--problem condensed">Problem</h2>
      <ul class="issue-list">
        <li>Your exterior semi-transparent deck, fence or siding is peeling, chipping or faded.</li>
        <li>Your deck or fence is chipping or peeling, and looks old and faded.</li>
        <li>Your exterior windows, doors, garage doors, stucco, siding, soffits are chipping or peeling, and look old and faded.</li>
        <li>Is the colour in your interior basement, kitchen, bedrooms and bathrooms walls, doors, and trim faded or out-of-date?</li>
      </ul>
      <h2 class="panel-tag panel-tag--solution condensed">Solution</h2>
      <ul class="issue-list">
        <li>A fresh coat of stain to protect the wood and make it look clean, fresh and beautiful!</li>
        <li>A fresh coat of stain will protect your investment and make it look clean, fresh and Beautiful again!</li>
        <li>A fresh coat of paint to make your interior look clean, fresh and beautiful again!</li>
      </ul>
    </div>
    <div class="call-band condensed">
      <span class="call-label">CALL NOW</span>
      <span class="phone-back">555-013-4821</span>
    </div>

    <div class="brand">
      <span class="brand-ring"></span>
      <span class="brand-name">Brightwall Coaters</span>
    </div>

    <div class="stamp-box"></div>
    <span class="address-line" style="top:250px"></span>
    <span class="address-line" style="top:298px"></span>
    <span class="address-line" style="top:348px"></span>
  </section>

</main>
</body>
</html>
```